UK Loan Company wanting to send a Christmas themed flyer to closed customers offering credit.

We need an A5 design. We want to invite closed customers back to our business by providing a flyer which contains a blank box where we can print how much credit we can offer. (We will add the amount ourselves)

Any customers who reopen their account has chance to win a laptop!

See attached word document for further information

Target Market(s)

UK home credit

Font styles to use
Serif
Sans Serif

Colors

Designer to choose colors to be used in the design.

Requirements
Must have
• our company logo see www.maplecrestfin.co.uk
• Seasons Greetings Title (see attached word draft)
• Credit Blank Box
• Representative example
• Authorised and regulated by The Marsden Standards Board
Nice to have
• Vouchtree logo and store outlets?

```html
<!DOCTYPE html>
<html lang="en">
<head>
<meta charset="utf-8">
<title>Maplecrest – Season's Greetings Flyer</title>
<link rel="stylesheet" href="https://fonts.googleapis.com/css2?family=Great+Vibes&family=Didact+Gothic&display=swap">
<style>
  :root {
    --sky: #4bbdeb;
    --navy: #253a7c;
    --ink: #111111;
    --muted: #444444;
    --paper: #ffffff;
    --box-line: #7a7a7a;
  }
  * { margin: 0; padding: 0; box-sizing: border-box; }
  html, body {
    width: 846px; height: 1200px; overflow: hidden;
    background: var(--sky);
  }
  .flyer {
    position: relative;
    width: 846px; height: 1200px;
    background: var(--sky);
    font-family: "Didact Gothic", "Century Gothic", sans-serif;
    color: var(--ink);
  }
  .sheet {
    position: absolute;
    left: 31px; top: 30px; width: 784px; height: 1140px;
    background: var(--paper);
    border: 2px solid var(--navy);
    box-shadow: 3px 4px 6px rgba(0,0,0,0.35);
  }
  .block {
    position: absolute; left: 0; width: 100%;
    text-align: center; white-space: nowrap;
  }
  .brand {
    position: absolute; left: 30px; top: 36px;
    display: flex; align-items: center; gap: 8px;
  }
  .brand-dot {
    width: 14px; height: 14px; background: var(--sky);
  }
  .brand-name {
    font-size: 17px; line-height: 20px;
    color: var(--navy);
  }
  .partner {
    position: absolute; right: 30px; top: 30px;
    display: flex; align-items: center; gap: 8px;
  }
  .partner-dot {
    width: 30px; height: 30px; border-radius: 50%;
    background: var(--sky);
  }
  .partner-name {
    font-size: 19px; color: #333333; letter-spacing: 1px;
  }
  .title {
    top: 122px;
    font-family: "Great Vibes", cursive;
    font-size: 86px; line-height: 100px;
    color: var(--sky);
    text-shadow: 1px 1px 0 #1d4f6a, 2px 2px 2px rgba(0,0,0,0.25);
  }
  .invite {
    top: 281px;
    font-size: 19px; line-height: 25.6px;
  }
  .offer-heading {
    top: 368px;
    font-size: 18.5px; line-height: 24px;
    font-weight: 700; letter-spacing: 0.2px;
  }
  .credit-box {
    position: absolute; left: 244px; top: 399px;
    width: 298px; height: 96px;
    border: 1px solid var(--box-line);
  }
  .rep-example {
    top: 566px;
    font-size: 19px; line-height: 25.6px;
  }
  .terms {
    top: 648px;
    font-size: 19px; line-height: 25.6px;
    color: var(--muted);
  }
  .prize-band {
    position: absolute; left: 46px; top: 727px;
    width: 690px; height: 54px;
    background: var(--sky);
    display: flex; align-items: center; justify-content: center;
    text-align: center; white-space: nowrap;
    font-style: italic; font-weight: 700;
    font-size: 16.5px; line-height: 20px;
    color: var(--navy);
  }
  .contact-heading {
    top: 892px;
    font-size: 25px; line-height: 30px;
  }
  .contact-phone {
    top: 921px;
    font-size: 36px; line-height: 44px;
    font-weight: 700; letter-spacing: 1px;
  }
  .legal {
    top: 1026px;
    font-size: 19px; line-height: 25.6px;
  }
</style>
</head>
<body>
<main class="flyer">
  <section class="sheet">
    <header>
      <div class="brand">
        <span class="brand-dot"></span>
        <span class="brand-name">Maplecrest Financial Services (Yorkshire) Limited</span>
      </div>
      <div class="partner">
        <span class="partner-dot"></span>
        <span class="partner-name">VOUCHTREE</span>
      </div>
    </header>

    <h1 class="block title">Season's Greetings</h1>

    <p class="block invite">As a valued previous customer, we would like to invite you to reopen your<br>account and have a chance to win a Laptop. Treat yourself with one of our<br>cash loans or Vouchtree vouchers which would make an ideal gift.</p>

    <h2 class="block offer-heading">WE WOULD BE DELIGHTED TO OFFER YOU CREDIT OF UP TO</h2>

    <div class="credit-box" aria-label="Credit amount"></div>

    <p class="block rep-example">Representative example: Loan amount £150.00 payable over 22 weeks at<br>£10.50 per week. Interest is £81.00. The Total amount payable is £231.00.<br>Interest rate is 127.99% per annum (fixed). 716.47% APR representative.</p>

    <p class="block terms">Terms and conditions apply. All credit is subject to status &amp; affordability.<br>Written quotations on request</p>

    <div class="prize-band">All customers that reopen their accounts with us before the 18th December 2019<br>will be entered into our free prize with the chance to win a 17” Vantro Laptop.</div>

    <p class="block contact-heading">FOR MORE INFORMATION CONTACT OUR OFFICE ON</p>
    <p class="block contact-phone">01632 960 418</p>

    <footer class="block legal">Authorised and regulated by The Marsden Standards Board. Contact<br>address: Maplecrest Financial Services (Yorkshire) Ltd, Harbour House,<br>Kestrel Business Park, Alder Way, Wakefield WF9 4ZX.<br>Registered in England No 5820613</footer>
  </section>
</main>
</body>
</html>
```